Eco conscious print and frame company needs a website

‘VURleaf is a new company that makes frames and fine art prints from sustainable bamboo. Our site should have an organic feel yet still have a professional clean look to it as well.
We need shopping cart and image uploading capabilities much like a pixelbarn or photomoth type of site only on a much smaller scale.
Currently we have 3 different styles available in sizes from 8"x8" all the way to 4ft by 8ft.
Target audience will be the lumograffic, picturely, zaphone market.

Target Market(s)

20-40 years old male and female. Picturely generation.

Industry/Entity Type

Shopping

Requirements
Must have
• Front end and back end capabilities with emphasis on image uploading and shopping cart functionality.

```html
<!DOCTYPE html>
<html lang="en">
<head>
<meta charset="utf-8">
<title>VURleaf Frame Company</title>
<link href="https://fonts.googleapis.com/css2?family=Ubuntu:wght@300;400;500&display=swap" rel="stylesheet">
<style>
:root{
  --ink:#1f1f1f;
  --bar:#232323;
  --green-top:#a9d13a;
  --green-mid:#8cc21c;
  --green-low:#7db515;
  --accent:#7aab0a;
  --accent-soft:#6a9c10;
  --white:#ffffff;
  --text:#2b2b2b;
  --muted:#555;
  --foot-top:#e3e3e3;
  --foot-low:#fbfbfb;
}
*{box-sizing:border-box;margin:0;padding:0}
html,body{width:1200px;height:1162px;overflow:hidden}
body{position:relative;background:var(--white);font-family:"Ubuntu",sans-serif;color:var(--text)}
.abs{position:absolute}
.topbar{left:0;top:0;width:1200px;height:14px;background:var(--bar)}
.hero{left:0;top:14px;width:1200px;height:468px;background:radial-gradient(ellipse at 25% 30%,var(--green-top),var(--green-mid) 55%,var(--green-low))}
.cart-tab{left:788px;top:0;width:285px;height:38px;background:var(--bar);border-radius:0 0 8px 8px;color:#eee;font-size:12px;display:flex;align-items:center;padding-left:14px;gap:8px;padding-top:4px}
.cart-tab svg{flex:none}
.main-nav{left:483px;top:62px;display:flex}
.main-nav a{color:var(--white);text-decoration:none;font-size:16.5px;line-height:38px;padding:0 12px}
.main-nav a.current{background:var(--white);color:var(--ink);border-radius:7px;padding:0 14px}
.brand-mark{left:238px;top:90px;width:140px;height:140px;border-radius:50%;background:rgba(60,110,20,.35)}
.brand-name{left:130px;top:250px;font-size:84px;font-weight:300;color:var(--ink);letter-spacing:-1px;line-height:1}
.brand-tag{left:216px;top:346px;font-size:21px;font-weight:300;color:#d9ec9c;letter-spacing:1px}
.upload-btn{left:150px;top:461px;width:318px;height:40px;background:var(--bar);border-radius:10px 0 0 10px;color:var(--white);font-size:22px;line-height:41px;padding-left:18px;letter-spacing:.5px}
.upload-icon{left:436px;top:462px;width:44px;height:40px;background:linear-gradient(135deg,#cfe3f2,#7a8fa8);transform:rotate(-12deg);border:3px solid var(--white)}
.conditions h3{position:absolute;left:156px;top:512px;font-size:17px;font-weight:400;color:var(--ink)}
.conditions p{position:absolute;left:159px;top:539px;width:313px;font-size:11px;line-height:15px;text-align:justify;color:var(--muted)}
.slider{left:528px;top:118px;width:533px;height:420px;background:var(--white);border:1px solid #d7e7b5;box-shadow:inset 0 0 0 4px rgba(140,194,28,.25)}
.slide-photo{left:547px;top:136px;width:496px;height:383px;background:linear-gradient(160deg,#b6cf4a,#6d8a23 45%,#c9d77a 75%,#9bb83a)}
.framed-print{left:772px;top:306px;width:262px;height:262px;transform:rotate(-10deg);background:linear-gradient(135deg,#e7c0ad,#d09c86);box-shadow:2px 4px 8px rgba(0,0,0,.35)}
.framed-print span{position:absolute;left:24px;top:24px;right:24px;bottom:24px;background:#151515;padding:8px}
.framed-print span i{display:block;width:100%;height:100%;background:linear-gradient(160deg,#b8d04a,#6e8c24 50%,#a6c040)}
.slider-arrows{left:535px;top:546px}
.welcome-band{left:0;top:614px;width:1200px;height:26px;background:var(--bar)}
.welcome-band h2{position:absolute;left:441px;top:0;font-size:23px;font-weight:500;color:var(--accent);line-height:27px}
.book-art{left:176px;top:652px;width:200px;height:202px;background:linear-gradient(140deg,#f4efe8,#e8b38a 45%,#9cb75a 70%,#b43a3a);border-radius:3px}
.intro{left:443px;top:660px;width:602px;font-size:12px;line-height:24px;color:var(--text)}
.intro p{text-align:justify;text-align-last:left}
.footer{left:0;top:863px;width:1200px;height:273px;background:linear-gradient(var(--foot-top),var(--foot-low));border-top:1px solid #cfcfcf}
.foot-col h4{font-size:17px;font-weight:400;color:var(--ink);margin-bottom:14px}
.foot-col ul{list-style:none;font-size:13px;line-height:16.8px;color:var(--ink)}
.pay-title{left:751px;top:883px;font-size:17px;color:var(--accent);font-weight:400}
.pay-cards{left:751px;top:912px;display:flex;gap:10px}
.pay-cards span{width:67px;height:36px;background:var(--white);border:1px solid #d8d8d8;font-size:11px;font-weight:500;color:var(--accent-soft);display:flex;align-items:center;justify-content:center}
.ship-note{left:755px;top:971px;font-size:13px;color:var(--accent-soft)}
.follow{left:750px;top:1013px;font-size:17px;color:var(--ink)}
.social{left:748px;top:1043px;display:flex;gap:4px}
.social span{width:44px;height:44px;background:var(--white);border:1px solid #cfcfcf;border-radius:5px;box-shadow:0 1px 2px rgba(0,0,0,.15);font-size:9px;color:var(--ink);display:flex;align-items:center;justify-content:center}
.code{left:1018px;top:1093px;font-size:11px;color:var(--ink)}
.bottombar{left:0;top:1136px;width:1200px;height:26px;background:var(--bar)}
.bottombar p{position:absolute;left:935px;top:8px;font-size:11px;color:#ddd}
</style>
</head>
<body>
<div class="abs topbar"></div>
<header class="abs hero"></header>

<div class="abs cart-tab">
  <svg width="18" height="18" viewBox="0 0 18 18"><rect x="1" y="3" width="13" height="13" fill="#fff"/><path d="M4 9l3 3 8-10" stroke="#d33" stroke-width="2.5" fill="none"/></svg>
  <span>Check out &nbsp;|</span>
  <svg width="16" height="18" viewBox="0 0 16 18"><rect x="1" y="5" width="14" height="12" rx="1" fill="#f2a900"/><path d="M5 6V3a3 3 0 016 0v3" stroke="#f2a900" fill="none" stroke-width="1.5"/></svg>
  <span>Shopping cart : (0)</span>
</div>

<nav class="abs main-nav">
  <a class="current" href="#">Home</a><a href="#">About</a><a href="#" style="padding-left:16px">Products</a><a href="#">Photo Mugs</a><a href="#">Photo Books</a><a href="#">Special Offer</a>
</nav>

<div class="abs brand-mark"></div>
<div class="abs brand-name">’VURleaf</div>
<div class="abs brand-tag">FRAME COMPANY</div>

<div class="abs upload-btn">UPLOAD YOUR PHOTOS</div>
<div class="abs upload-icon" role="img" aria-label="Small stack of photos icon"></div>
<section class="conditions">
  <h3>Conditions</h3>
  <p>Photo size should be XX.XXPixels and resolution should be 150dpi and clear photo can you upload it.</p>
</section>

<div class="abs slider"></div>
<div class="abs slide-photo" role="img" aria-label="Photo of a sunlit green park path with a woman sitting by a fence"></div>
<div class="abs framed-print" role="img" aria-label="Bamboo framed print of the same park photo"><span><i></i></span></div>
<svg class="abs slider-arrows" width="34" height="20" viewBox="0 0 34 20"><path d="M15 1v18L1 10z" fill="#6fa70b"/><path d="M19 1v18l14-9z" fill="#6fa70b"/></svg>

<div class="abs welcome-band"><h2>Welcome to Our Website</h2></div>
<div class="abs book-art" role="img" aria-label="Open photo book showing family pictures"></div>
<div class="abs intro">
  <p>Lorem ipsum dolor sit amet, consectetur adipisicing elit, sed do eiusmod tempor incididunt ut labore et dolore magna aliqua. Ut enim ad minim veniam, quis nostrud exercitation ullamco laboris nisi ut aliquip ex ea commodo consequat. Duis aute irure dolor in reprehenderit in voluptate velit esse cillum dolore eu fugiat nulla pariatur. Excepteur sint occaecat cupidatat non proident, sunt in culpa qui officia deserunt mollit anim id est laborum.veniam, quis nostrud exercitation ullamco laboris nisi ut</p>
  <p>aliquip ex ea commodo consequat. Duis aute irure dolor in reprehenderit in voluptate velit esse cillum dolore eu fugiat nulla pariatur. Excepteur sint occaecat cupidatat non proident, sunt in culpa qui officia deserunt mollit anim id est laborum.</p>
</div>

<footer class="abs footer"></footer>
<div class="abs foot-col" style="left:177px;top:885px">
  <h4>Shop with us</h4>
  <ul><li>Calendars</li><li>Canvas Prints</li><li>Cards</li><li>Collage Gifts</li><li>Collage Prints</li><li>Mousepads</li><li>Mugs</li><li>Photo Books</li><li>Posters</li><li>Prints</li><li>Pricing</li><li>Shop all products</li></ul>
</div>
<div class="abs foot-col" style="left:345px;top:884px">
  <h4>Our services</h4>
  <ul style="padding-left:2px"><li>Email Upload</li><li>Flickpost Printing</li><li>Free photo sharing online</li><li>Free, unlimited storage</li><li>Free photo software</li><li>Mobile</li></ul>
</div>
<div class="abs foot-col" style="left:548px;top:885px">
  <h4 style="margin-left:1px">Customer care</h4>
  <ul><li>Contact Customer Support</li><li>Help</li><li>Site map</li><li>Where is my order?</li></ul>
</div>
<div class="abs foot-col" style="left:546px;top:1007px">
  <h4>About VURleaf</h4>
  <ul><li>About us</li><li>Privacy policy</li><li>Terms &amp; conditions</li></ul>
</div>

<div class="abs pay-title">PAYMENT METHODS</div>
<div class="abs pay-cards"><span>Vantapay</span><span>PayWell</span><span>MeritCard</span><span>Amberline</span></div>
<div class="abs ship-note">Products shipped across India in 3-7 working days</div>
<div class="abs follow">Follow us on</div>
<div class="abs social"><span>Facenote</span><span>Chirper</span><span>Feed</span></div>
<div class="abs code">M1</div>

<div class="abs bottombar"><p>© 2012.www.vurleaf.com</p></div>
</body>
</html>
```